A new Blog: Turning Over New Leaves

I need a wordpress blog design for my new blog called Turning Over New Leaves.

I'm not an alcoholic. I certainly don't think I am, and I'm fairly certain that if you spoke to my friends and family they would agree that I don't have any issues with substance abuse. I definitely enjoy a drink. A few beers, gin and tonic's or a nice red wine (along with a few cigarettes) have been particular vices for the last few years of my life.

But no more. I'm going 365 with no alcohol and I am giving up cigarettes.

Why? I have my reasons... and this blog will reveal those and chronicle my year long journey.

The blog is called Turning Over New Leaves and I want a clean, crisp design to reflect this new adventure.

I'm looking for a design that is unique and not the same as every other blog you see. I want my readers to feel uplifted when they see it.

Most importantly, the blog needs to be simple for me to use and modify (add a new page if needed in the future)
Updates

Reason: To allow time for designers to submit revised designs.

Reason: My apologies designers, I haven't had an opportunity to provide feedback to enable changes. I will be doign this tomorrow morning and so am extending the deadline to allow resubmission.

Regards, Dale.

Target Market(s)

My target market are males and females, 17-28 in western speaking countries

Requirements
Must have
• - A graphic banner/branding featuring the blog title. This should be able to be used as a small stand alone logo.
- Ability to show my latest tweets
- A connect box where people can click on Chatterloop, Peepstream and Postvane links to contact me
- A widget that is showing how many days I am into the 365 day challenge (this should feature prominently)
- A widget that shows how much money as the challenge progresses
- It should have an ability to subcribe to the blog (RSS feeds)
- There needs to be an about me page
- There should be a blog roll
- There should be a list of categories/tags displayed somewhere (do something creative with this, find a way to make what I am talking about most more prominent!)
- A recent post link box somewhere at the side to encourage people to keep reading
- Recent comment links
- A search functionality
- An advertisement side bar (only a small amount of advertising will be done - so don't make it too prominent!)

Nice to have
• Without crowding the design it would also be good to have
-Popular post links (the most highly trafficked or commented) posts.

I'm excited to hear what other things YOU THINK should feature. Surprise me! I will reward innovation.

```html
<!DOCTYPE html>
<html lang="en">
<head>
<meta charset="utf-8">
<title>Turning Over New Leaves</title>
<link rel="stylesheet" href="https://fonts.googleapis.com/css2?family=PT+Sans:wght@400;700&family=PT+Sans+Narrow&family=Arimo&display=swap">
<style>
:root{
  --cream:#f7f1d0;
  --cream-band:#ece3b6;
  --sky-top:#bfe4ee;
  --sky-mid:#2db8e6;
  --grass:#7fb24a;
  --paper:#ffffff;
  --side:#e9ebea;
  --widget:#f2f2f2;
  --widget-edge:#2b9ee0;
  --ink:#555555;
  --ink-dark:#222222;
  --blue:#1a8fd6;
  --white:#ffffff;
}
*{box-sizing:border-box;margin:0;padding:0}
html,body{width:800px;height:1200px;overflow:hidden}
body{position:relative;background:var(--cream);font-family:"Arimo",Arial,sans-serif;color:var(--ink)}
.backdrop-sky{position:absolute;left:0;top:0;width:800px;height:240px;
  background:linear-gradient(180deg,var(--sky-top) 0%,#d9eef0 55%,#a9c98a 80%,#8fba5c 100%)}
.backdrop-band{position:absolute;left:0;top:965px;width:800px;height:20px;background:var(--cream-band)}
.backdrop-lower{position:absolute;left:0;top:985px;width:800px;height:215px;
  background:linear-gradient(180deg,#efe6bf,#f8f3da)}
.page{position:absolute;left:68px;top:52px;width:664px;height:1096px;background:var(--paper);
  border-radius:22px;box-shadow:0 6px 18px rgba(0,0,0,.35);overflow:hidden}
.masthead{position:absolute;left:0;top:0;width:664px;height:170px;
  background:linear-gradient(180deg,#1aa6df 0%,#37c3ec 45%,#a6d9d6 72%,#86bd52 88%,#5c9a2e 100%)}
.blog-title{position:absolute;left:40px;top:40px;width:600px;text-align:center;color:var(--white);
  font-family:"PT Sans",sans-serif;font-size:52px;font-variant:small-caps;letter-spacing:1px;white-space:nowrap;
  text-shadow:0 1px 3px rgba(0,0,0,.2)}
.main-nav{position:absolute;left:58px;top:144px;display:flex;gap:13px;color:var(--white);
  font-family:"PT Sans",sans-serif;font-size:11.5px;font-weight:700;white-space:nowrap}
.main-nav .social{display:flex;gap:9px}
.binding{position:absolute;left:0;top:170px;width:664px;height:24px;
  background:linear-gradient(180deg,#d7d7d7,#9e9e9e 50%,#eeeeee)}
.hero-photo{position:absolute;left:20px;top:0;width:240px;height:200px;border-radius:40% 40% 30% 30%;
  background:radial-gradient(ellipse at 50% 50%,rgba(112,140,175,.85),rgba(160,180,200,.35) 60%,rgba(200,220,230,0) 75%)}
.content{position:absolute;left:105px;top:272px;width:392px}
.intro{font-size:14px;line-height:16px;color:var(--ink);word-break:break-all}
.post{position:absolute;left:0;width:392px}
.post-date{color:var(--blue);font-size:13.5px;word-spacing:2px}
.post-date span{margin-left:22px}
.post-body{margin-top:1px;font-size:12px;line-height:14.5px;color:var(--ink);word-break:break-all}
.post-body b{font-weight:400;font-size:14px}
.post-photo{position:absolute;left:104px;top:913px;width:288px;height:206px;
  background:linear-gradient(160deg,#8e5c46 0%,#a89f95 40%,#c8c5bf 60%,#6d6a64 100%)}
.sidebar{position:absolute;left:528px;top:245px;width:204px;height:886px;
  background:linear-gradient(90deg,#dfe1e0,#f3f3f3 30%,#ececec)}
.widget{position:absolute;background:var(--widget);border-radius:10px;
  border-left:5px solid var(--widget-edge);border-right:5px solid var(--widget-edge);border-top:3px solid var(--widget-edge);
  box-shadow:0 4px 8px rgba(0,0,0,.25);text-align:center}
.widget-title{font-family:"PT Sans",sans-serif;font-variant:small-caps;color:var(--ink-dark);font-size:17px;font-weight:700}
.counter{left:545px;top:265px;width:170px;height:222px;padding-top:10px}
.counter .widget-title{font-size:13.5px;letter-spacing:.2px}
.counter .sub{font-family:"PT Sans Narrow",sans-serif;color:#8c8c8c;font-size:18px;line-height:18px}
.counter .note{font-family:"PT Sans Narrow",sans-serif;color:#8c8c8c;font-size:10px;margin-top:4px}
.pill{margin:5px auto 0;width:132px;height:22px;background:var(--white);border-radius:11px;
  font-family:"PT Sans Narrow",sans-serif;font-size:11px;color:var(--ink-dark);line-height:22px}
.pill i{font-style:normal;color:#bbb;margin:0 8px}
.money{margin-top:14px;font-family:"PT Sans Narrow",sans-serif;color:#8c8c8c;font-size:20px;line-height:20px}
.list-widget{width:166px;height:172px;padding-top:12px}
.popular{left:549px;top:518px}
.blogroll{left:549px;top:713px}
.list-card{margin:8px auto 0;width:126px;height:120px;background:var(--white);border-radius:6px;text-align:left;
  padding:8px 6px 0 14px;font-family:"PT Sans Narrow",sans-serif;font-size:10px;line-height:13px;color:var(--ink-dark);overflow:hidden}
.list-card li{margin-bottom:9px;word-break:break-all}
.advert{position:absolute;left:550px;top:906px;width:160px;height:221px;
  background:linear-gradient(180deg,#1f6fc2 0%,#3c8fdc 40%,#8fb9e6 75%,#e6eef6 100%)}
</style>
</head>
<body>
<div class="backdrop-sky"></div>
<div class="backdrop-band"></div>
<div class="backdrop-lower"></div>

<div class="page">
  <header class="masthead">
    <h1 class="blog-title">Turning Over New Leaves</h1>
    <nav class="main-nav">
      <span>about me</span><span>blogs</span><span>categories/tags</span><span>recent comments</span><span>galleries</span>
      <span class="social">follow me at <span>Chatterloop</span><span>Peepstream</span><span>Postvane</span></span>
    </nav>
  </header>
  <div class="binding"></div>
</div>

<div class="hero-photo" role="img" aria-label="Photo of a young man leaping for joy in jeans"></div>

<div class="sidebar"></div>

<main class="content">
  <p class="intro">Hi abskjjs /klss lksdjjp dljpon;ov[pf sd;l'sd kdlkdn'd'sdm'sd;d d;dd /klss lksdjjp dljpon;ov[pf sd;l'sd kdlkdn'd'sdm'sd;dd;dd dmd;mvmf lmv'fdmvfmv mv;mv;d sdknvdkd;ofot. dl;flfbm;fm vffdfmfm;fmbb;'fnvfnsnf dfnldfn dfklvndfli v/df;e v;dmd;mv.</p>
</main>

<article class="post" style="left:105px;top:380px">
  <div class="post-date">Fri. 01 Feb. 2011<span>08:22:19 GMT</span></div>
  <p class="post-body"><b>I'ts the first day of life to chaleenge my self to</b> escape from the viceskdlkdn'd'sdm'sd;dd;dd /klsslksdjjp dljpon;ov[pf sd;l'sd kdlkdn'd'sdm'sd;dd;dddmd;mvmf lmv'fdmvfmv mv;mv;d sdknvdkd;ofot. dl;flfbm;fmvffdfmfm;fmbb;'fnvfnsnf dfnldfn dfklvndfli v/df;e v;dm.o chaleenge my self to escape from the viceskdlkdn'd'sdm'sd;dd;dd /klsslksdjjp dljpon;ov[pf sd;l'sd kdlkdn'd'sdm'sd;dd;dddmd;mvmf lmv'fdmvfmv mv;mv;d sdknvdkd;ofot. dl;flfbm;fmvffdfmfm;fmbb;'fnvfnsnf dfnldfn dfklvndfli v/df;e v;dm.</p>
</article>

<article class="post" style="left:104px;top:583px">
  <div class="post-date">Sat. 02 Feb. 2011<span>07:42:19 GMT</span></div>
  <p class="post-body"><b>I'ts the second day of life to chaleenge my self to</b> escape from the viceskdlkdn'd'sdm'sd;dd;dd /klsslksdjjp dljpon;ov[pf sd;l'sd kdlkdn'd'sdm'sd;dd;dddmd;mvmf lmv'fdmvfmv mv;mv;d sdknvdkd;ofot. dl;flfbm;fmvffdfmfm;fmbb;'fnvfnsnf dfnldfn dfklvndfli v/df;e v;dm.o chaleenge my self to escape from the viceskdlkdn'd'sdm'sd;dd;dd /klsslksdjjp dljpon;ov[pf sd;l'sd kdlkdn'd'sdm'sd;dd;dddmd;mvmf lmv'fdmvfmv mv;mv;d sdknvdkd;ofot. dl;flfbm;fmvffdfmfm;fmbb;'fnvfnsnf dfnldfn dfklvndfli v/df;e v;dm.</p>
</article>

<article class="post" style="left:102px;top:780px">
  <div class="post-date">Sun. 03 Feb. 2011<span>01:38:17 GMT</span></div>
  <p class="post-body"><b>I'ts the third day of life to chaleenge my self to</b> escape from the viceskdlkdn'd'sdm'sd;dd;dd /klsslksdjjp dljpon;ov[pf sd;l'sd kdlkdn'd'sdm'sd;dd;dddmd;mvmf lmv'fdmvfmv mv;mv;d sdknvdkd;ofot. dl;flfbm;fmvffdfmfm;fmbb;'fnvfnsnf dfnldfn dfklvndfli v/df;e v;dm.o chaleenge my self to escape from the viceskdlkdn'd'sdm'sd;dd;dd /klsslksdjjp dljpon;ov[pf sd;l'sd kd;ofot. dl;flfbm;fmvffdfmfm;fmbb;'fnvfnsnf dfnldfn dfklvndfli v/df;e v;dm.</p>
</article>

<div class="post-photo" role="img" aria-label="Photo of cigarette butts stuffed into a concrete ashtray bin"></div>

<aside class="widget counter">
  <h2 class="widget-title">Turning Over New Leaves</h2>
  <div class="sub">Day Counter</div>
  <div class="note">I stopped smoking on</div>
  <div class="pill">March<i>|</i>05<i>|</i>2011</div>
  <div class="note">It has been...I quit</div>
  <div class="pill">0 weeks<i>|</i>01 day<i>|</i>0:8 mins.</div>
  <div class="money">Money Saved</div>
  <div class="note" style="margin-top:0">by choosing not to smoke.</div>
  <div class="pill">AU$ 0,000,1.00</div>
</aside>

<aside class="widget list-widget popular">
  <h2 class="widget-title">Popular Post</h2>
  <ul class="list-card">
    <li>stopped smoking on vddjnv nvlflklfkfkk lklk lk slk.</li>
    <li>cm;mvlkmvlsmmlkm;sdfmv sv skm;mv;md;kvm.</li>
    <li>dkvnsmvlsdvlkdssdkmn'ldk dfnvln</li>
  </ul>
</aside>

<aside class="widget list-widget blogroll">
  <h2 class="widget-title">Blogs</h2>
  <ul class="list-card">
    <li>stopped smoking on vddjnv nvlflklfkfkk lklk lk slk.</li>
    <li>m;mvlkmvlsmmlkm;sdfmv sv skm;mv;md;kvm.</li>
    <li>dkvnsmvlsdvlkdssdkmn'ldk dfnvln</li>
  </ul>
</aside>

<div class="advert" role="img" aria-label="Advertisement for a men's multivitamin supplement"></div>
</body>
</html>
```